Aerospace Private Equity Firm Needs Website

We need a website for new private equity fund called Orlin Partners. We buy smaller companies in the aerospace and industrial industries. I have attached some information about the firm. An example of a site we like that is a similar business but focused in a different sector is www.travomedic.com. www.quarnestgrove.com is a firm that also invests in aerospace companies.

Industry/Entity Type

Equity

Number of Pages Required

1 page

Colors
0555a3
33a6d7
ec1f27

```html
<!DOCTYPE html>
<html lang="en">
<head>
<meta charset="utf-8">
<title>Orlin Partners</title>
<link rel="stylesheet" href="https://fonts.googleapis.com/css2?family=Questrial&family=Lato:wght@400;700&display=swap">
<style>
  :root {
    --navy: #0a3a8a;
    --brand-blue: #0555a3;
    --sky: #33a6d7;
    --red: #ec1f27;
    --deep-red: #c8101a;
    --ink: #1b1b1b;
    --white: #ffffff;
    --footer: #050505;
  }
  * { box-sizing: border-box; margin: 0; padding: 0; }
  html, body { width: 1200px; height: 972px; overflow: hidden; background: var(--white); }
  body { position: relative; font-family: "Lato", sans-serif; color: var(--ink); }

  .hero {
    position: absolute; left: 0; top: 92px; width: 1200px; height: 533px;
    background:
      linear-gradient(180deg, rgba(20,20,30,0.25) 0%, rgba(20,20,30,0.15) 60%, rgba(10,10,10,0.55) 100%),
      linear-gradient(180deg, #aab4c4 0%, #c9ced6 22%, #6f7f5c 38%, #58704a 55%, #8c6a52 75%, #7a5546 100%);
  }

  .site-header { position: absolute; left: 0; top: 0; width: 1200px; height: 108px; }
  .site-header svg { position: absolute; left: 0; top: 0; }
  .brand {
    position: absolute; left: 82px; top: 30px;
    display: flex; align-items: center; gap: 10px;
    font-family: "Questrial", sans-serif; font-size: 34px; color: var(--navy);
  }
  .brand-dot { width: 14px; height: 14px; border-radius: 50%; background: var(--red); }

  .main-nav a {
    position: absolute; top: 51px;
    font-family: "Questrial", sans-serif; font-size: 18px; color: var(--white);
    text-decoration: none; white-space: nowrap;
  }
  .nav-sep { position: absolute; top: 57px; width: 1px; height: 13px; background: #4d7fc8; }

  .sectors { position: absolute; top: 397px; left: 0; width: 1200px; }
  .sector { position: absolute; width: 180px; text-align: center; }
  .sector-badge {
    width: 148px; height: 148px; margin: 0 auto; border-radius: 50%;
    background: var(--navy); border: 3px solid var(--white);
    display: flex; align-items: center; justify-content: center;
  }
  .sector-label {
    margin-top: 12px; font-family: "Questrial", sans-serif; font-size: 28px;
    color: var(--white); text-shadow: 0 2px 4px rgba(0,0,0,0.6);
  }

  .welcome { position: absolute; top: 660px; left: 0; width: 1200px; text-align: center; }
  .welcome-title {
    font-family: "Questrial", sans-serif; font-weight: 400; font-size: 38px;
    color: var(--navy); letter-spacing: 1px;
  }
  .welcome-copy {
    width: 1000px; margin: 40px auto 0; font-size: 15.5px; line-height: 24px; color: var(--ink);
  }
  .read-more {
    position: absolute; left: 520px; top: 183px; width: 160px; height: 40px;
    border-radius: 20px; background: var(--deep-red);
    display: flex; align-items: center; padding-left: 20px;
    font-family: "Questrial", sans-serif; font-size: 17px; color: var(--white); text-decoration: none;
  }
  .read-more-arrow {
    position: absolute; right: 6px; top: 7px; width: 27px; height: 27px; border-radius: 50%;
    background: var(--navy); display: flex; align-items: center; justify-content: center;
  }

  .site-footer {
    position: absolute; left: 0; top: 923px; width: 1200px; height: 49px; background: var(--footer);
  }
  .copyright {
    position: absolute; left: 80px; top: 16px; font-size: 15px; font-weight: 700; color: var(--white);
  }
  .social { position: absolute; top: 7px; width: 35px; height: 35px; border-radius: 50%; border: 2px solid #d8d8d8; }
  .social-a { left: 994px; background: #3b5a9a; }
  .social-b { left: 1038px; background: #1a7bb8; }
  .social-c { left: 1082px; background: #2fa6dd; }
</style>
</head>
<body>
  <div class="hero" role="img" aria-label="Aerial photo of a hillside city centre with tall glass office towers, red-roofed buildings and a crane"></div>

  <header class="site-header">
    <svg width="1200" height="108" viewBox="0 0 1200 108">
      <path d="M0,0 H1200 V36 H365 C335,36 318,62 300,85 C290,98 280,105 260,105 H0 Z" fill="var(--white)"/>
      <path d="M365,36 H1200 V92 H305 C322,68 338,36 365,36 Z" fill="var(--brand-blue)"/>
      <path d="M0,105 H260 C280,105 290,98 300,85 C318,62 335,36 365,36 H1200" fill="none" stroke="var(--red)" stroke-width="2"/>
    </svg>
    <div class="brand"><span>Orlin Partners</span><span class="brand-dot"></span></div>
    <nav class="main-nav">
      <a href="#" style="left:376px">Home</a>
      <span class="nav-sep" style="left:438px"></span>
      <a href="#" style="left:452px">Team</a>
      <span class="nav-sep" style="left:510px"></span>
      <a href="#" style="left:525px">Investment Strategy</a>
      <span class="nav-sep" style="left:698px"></span>
      <a href="#" style="left:713px">Portfolio Companies</a>
      <span class="nav-sep" style="left:893px"></span>
      <a href="#" style="left:907px">Press Releases</a>
      <span class="nav-sep" style="left:1038px"></span>
      <a href="#" style="left:1053px">Contact</a>
    </nav>
  </header>

  <section class="sectors">
    <div class="sector" style="left:344px">
      <div class="sector-badge">
        <svg width="76" height="76" viewBox="0 0 76 76">
          <g transform="rotate(45 38 38)" fill="var(--white)">
            <path d="M35,4 C35,1 41,1 41,4 V30 L70,46 V53 L41,44 V62 L50,69 V74 L38,70 L26,74 V69 L35,62 V44 L6,53 V46 L35,30 Z"/>
          </g>
        </svg>
      </div>
      <div class="sector-label">Aerospace</div>
    </div>
    <div class="sector" style="left:675px">
      <div class="sector-badge">
        <svg width="72" height="76" viewBox="0 0 72 76">
          <path d="M6,8 C10,4 14,10 18,6 C20,4 24,5 26,6" fill="none" stroke="var(--white)" stroke-width="3"/>
          <path d="M8,14 H18 V44 L34,34 V44 L50,34 V44 L66,34 V72 H8 Z" fill="var(--white)"/>
          <rect x="16" y="54" width="8" height="7" fill="var(--navy)"/>
          <rect x="30" y="54" width="8" height="7" fill="var(--navy)"/>
          <rect x="44" y="54" width="8" height="7" fill="var(--navy)"/>
        </svg>
      </div>
      <div class="sector-label">industrial</div>
    </div>
  </section>

  <section class="welcome">
    <h1 class="welcome-title">Welcome To Orlin Partners</h1>
    <p class="welcome-copy">Orlin Partners (“Orlin”) is a Los Angeles, California-based private equity firm formed in 2016 by Principals from Linden Crest Associates (LCA). Orlin focuses on lower middle-market control investments in aerospace and industrial companies based in North America. The Orlin team has invested successfully in these sectors over a 10-year period while at LCA.</p>
    <a class="read-more" href="#">READ MORE
      <span class="read-more-arrow">
        <svg width="12" height="12" viewBox="0 0 12 12"><path d="M4,2 L8,6 L4,10" fill="none" stroke="var(--white)" stroke-width="2"/></svg>
      </span>
    </a>
  </section>

  <footer class="site-footer">
    <p class="copyright">Copyright © 2017 &nbsp;Orlin Partners. &nbsp; All Rights Reserved.</p>
    <a class="social social-a" href="#" aria-label="Social profile"></a>
    <a class="social social-b" href="#" aria-label="Social profile"></a>
    <a class="social social-c" href="#" aria-label="Social profile"></a>
  </footer>
</body>
</html>
```